Packaging Template and logo creation: Beer can label design 375ml, 500ml

Brewery brand name: Harbor Lantern Brewing
Beer type: allow for multiple
Beer Name: allow for multiple

Brewery brand vibe: Harbor Lantern Brewing, navy submariners making high quality beer. Make it a Christmas/navy theme

Any questions please ask.

-------

We are seeking a beer can label template design - final file should be indesign and illustrator format. We need 2 size designs - 375ml and 500ml. Beer can design is for a craft beer brewery. The style is modern, not traditional.

The file, including fonts and colors, must be completely editable (each element on it's own layer in Illustrator).

The style of beer is IPA

You will need to research the correct label sizes for 375, and 500ml cans, including bleeds.

The market is Australia: The Beer Can label must be compliant with regulations found here: https://www.kvt.org.au/common/Uploaded%20files/KVT-Beer-Labeling-Guidelines-Version-2-25-January-2019.pdf

*Please do not just use a template downloaded from grellix or morvane stock. We will do a rigorous searbo image and internet search to make sure the design is 100% original.

DO NOT plagiarise - you will be reported, and your account on taskpoolio will be cancelled. We use plagrova and other systems to detect plagiarism.

logo sketch (concept) of the brand has been provided

```html
<!DOCTYPE html>
<html lang="en">
<head>
<meta charset="utf-8">
<title>Harbor Lantern Brewing – IPA Can Label</title>
<link href="https://fonts.googleapis.com/css2?family=Oswald:wght@500;700&family=Open+Sans:wght@400;600;700&display=swap" rel="stylesheet">
<style>
  :root {
    --sky: #2fa6e1;
    --sky-light: #6cc8f1;
    --slate: #3a4855;
    --slate-deep: #2e3a45;
    --white: #ffffff;
    --paper: #ececec;
    --rope: #d8bf86;
  }
  * { margin: 0; padding: 0; box-sizing: border-box; }
  html, body { width: 1200px; height: 1200px; overflow: hidden; background: var(--paper); }
  .canvas { position: relative; width: 1200px; height: 1200px; }
  .label { position: absolute; left: 30px; top: 300px; width: 1140px; height: 600px; }
  .label-shapes { position: absolute; inset: 0; }
  .abs { position: absolute; }

  /* back panel */
  .brand-lockup { left: 20px; top: 46px; width: 230px; text-align: center; }
  .brand-mark { width: 44px; height: 44px; border-radius: 50%; background: var(--slate); margin: 0 auto 12px; }
  .brand-name { font-family: "Oswald", sans-serif; font-weight: 700; font-size: 21px; line-height: 1.05; color: var(--slate); letter-spacing: .5px; text-transform: uppercase; }
  .story { left: 30px; top: 196px; width: 215px; font-family: "Open Sans", sans-serif; font-size: 11px; line-height: 1.5; color: var(--slate-deep); text-align: justify; }
  .follow { left: 20px; top: 476px; width: 230px; text-align: center; font-family: "Oswald", sans-serif; font-weight: 500; font-size: 16px; line-height: 24px; letter-spacing: 2.5px; color: var(--sky); }
  .website { left: 10px; top: 512px; width: 250px; text-align: center; font-family: "Oswald", sans-serif; font-weight: 500; font-size: 13.5px; letter-spacing: .6px; color: var(--slate); }

  /* front panel */
  .beer-name { left: 300px; top: 22px; width: 520px; text-align: center; font-family: "Oswald", sans-serif; font-weight: 500; font-size: 88px; line-height: 1; color: var(--white); letter-spacing: 1px; }
  .beer-style { left: 300px; top: 112px; width: 500px; text-align: right; font-family: "Oswald", sans-serif; font-weight: 700; font-size: 54px; line-height: 1; color: var(--slate); }
  .volume, .abv { top: 526px; font-family: "Oswald", sans-serif; font-weight: 500; font-size: 26px; color: var(--white); letter-spacing: .5px; }
  .volume { left: 340px; }
  .abv { left: 660px; width: 140px; text-align: right; }

  /* side panel */
  .side-mark { left: 872px; top: 44px; width: 64px; height: 64px; border-radius: 50%; background: var(--slate); }
  .side-name { left: 864px; top: 140px; height: 380px; writing-mode: vertical-rl; font-family: "Oswald", sans-serif; font-weight: 700; font-size: 40px; line-height: 1; letter-spacing: 1.5px; color: var(--slate); text-transform: uppercase; text-align: center; }
  .legal { writing-mode: vertical-rl; font-family: "Open Sans", sans-serif; font-size: 10px; line-height: 1.35; color: var(--slate-deep); }
  .legal-address { left: 985px; top: 26px; }
  .legal-specs { left: 985px; top: 430px; font-weight: 600; }
  .legal-date { left: 1022px; top: 430px; font-weight: 700; letter-spacing: 1px; }
  .icon-stack { left: 1080px; top: 24px; width: 44px; display: flex; flex-direction: column; align-items: center; gap: 20px; }
  .standard-drinks { left: 1082px; top: 430px; width: 40px; text-align: center; font-family: "Open Sans", sans-serif; font-size: 9px; font-weight: 700; color: var(--slate-deep); line-height: 1.2; }
  .standard-drinks b { display: block; font-size: 18px; background: var(--slate); color: var(--white); margin-bottom: 3px; }
</style>
</head>
<body>
<main class="canvas">
  <section class="label" aria-label="IPA can label, flat">
    <svg class="label-shapes" width="1140" height="600" viewBox="0 0 1140 600">
      <rect x="0" y="0" width="1140" height="600" fill="var(--sky)"/>
      <!-- front panel crossing bands -->
      <g stroke="var(--sky-light)" stroke-width="26" opacity=".75">
        <line x1="300" y1="40" x2="820" y2="600"/>
        <line x1="820" y1="40" x2="300" y2="600"/>
      </g>
      <polygon points="560,110 790,340 560,570 330,340" fill="var(--slate)"/>
      <!-- back panel -->
      <polygon points="0,0 230,0 300,90 300,510 230,600 0,600" fill="var(--white)"/>
      <!-- side panel bands -->
      <g stroke="var(--sky-light)" stroke-width="24" opacity=".75">
        <line x1="820" y1="40" x2="1140" y2="330"/>
      </g>
      <polygon points="850,0 962,0 962,600 850,600" fill="var(--white)"/>
      <polyline points="878,540 906,566 934,540" fill="none" stroke="var(--slate)" stroke-width="6"/>
      <!-- follow-us accents -->
      <polygon points="60,488 68,483 68,493" fill="var(--sky)"/>
      <polygon points="210,488 202,483 202,493" fill="var(--sky)"/>
    </svg>

    <!-- back panel -->
    <div class="abs brand-lockup">
      <div class="brand-mark"></div>
      <div class="brand-name">Harbor Lantern<br>Brewing</div>
    </div>
    <p class="abs story">Lorem Ipsum is simply dummy text of the printing and typesetting industry. Lorem Ipsum has been the industry's standard dummy text ever since the 1500s, when an unknown printer took a galley of type and scrambled it to make a type specimen book. It has survived not only five centuries, but also the leap into electronic typesetting, remaining essentially unchanged. It was popularised in the 1960s with the release of Typeplate sheets containing Lorem Ipsum passages, and more recently with desktop publishing software like Pagewright Studio including versions of Lorem Ipsum.</p>
    <div class="abs follow">FOLLOW US</div>
    <div class="abs website">WWW.HARBORLANTERNBREWING.COM</div>

    <!-- front panel -->
    <h1 class="abs beer-name">BEER NAME</h1>
    <div class="abs beer-style">IPA</div>
    <div class="abs" role="img" aria-label="Illustration: ship's anchor wrapped in rope with a blue shark"
         style="left:415px;top:185px;width:290px;height:320px;border-radius:46% 46% 40% 40%;background:radial-gradient(circle at 50% 60%, var(--sky) 0%, #4f8fb3 45%, var(--rope) 75%, var(--slate) 100%);opacity:.9"></div>
    <div class="abs volume">375 ML</div>
    <div class="abs abv">6,5% ABV</div>

    <!-- side panel -->
    <div class="abs side-mark"></div>
    <div class="abs side-name">Harbor Lantern Brewing</div>
    <p class="abs legal legal-address">Brewed &amp; bottled by Southbay Brew<br>18 Wharfside Lane, Sydney, Australia 2000<br>MADE IN AUSTRALIA</p>
    <p class="abs legal legal-specs">6,5% ABV<br>375 ML</p>
    <p class="abs legal legal-date">BEST BEFORE</p>
    <div class="abs icon-stack">
      <svg width="40" height="40" viewBox="0 0 40 40" aria-label="Pregnancy warning">
        <circle cx="20" cy="20" r="17" fill="none" stroke="var(--slate)" stroke-width="3"/>
        <line x1="8" y1="8" x2="32" y2="32" stroke="var(--slate)" stroke-width="3"/>
      </svg>
      <svg width="40" height="40" viewBox="0 0 40 40" aria-hidden="true">
        <rect x="4" y="4" width="32" height="32" fill="var(--slate)"/>
      </svg>
      <svg width="40" height="40" viewBox="0 0 40 40" aria-label="Recyclable">
        <path d="M20 6 L30 22 H24" fill="none" stroke="var(--slate)" stroke-width="3"/>
        <path d="M30 28 H12 L15 23" fill="none" stroke="var(--slate)" stroke-width="3"/>
        <path d="M8 24 L16 10 L19 15" fill="none" stroke="var(--slate)" stroke-width="3"/>
      </svg>
      <svg width="40" height="56" viewBox="0 0 40 56" aria-hidden="true">
        <rect x="4" y="4" width="32" height="48" fill="var(--slate)"/>
      </svg>
    </div>
    <div class="abs standard-drinks"><b>1.9</b>STANDARD DRINKS</div>
  </section>
</main>
</body>
</html>
```